FREE Network Assessment image for landing page

This graphic will be on a landing page and on the left will be Text and a download button that we change and control. The graphic for this project will be to the right.
I will add an example of the landing page area so that it makes more sense.

Please include the text from the sample - the font needs to be the same style as what we are using on the left side!

The graphic needs to be a .png file, roughly 713 x 527 white background. Use discretion on design layout.

Colors are black, Red = PMS 1795 and Gray = Cool Gray 10

Thanks,
Tom Harwick

Target Market(s)

small businesses

Industry/Entity Type

Information Technology

Font styles to use
Other font styles liked:
• See sample

Requirements
Must have
• see description
Nice to have
• Possibly small technology related image to help enhance the text but I don't want any image to compete with the text. Keep in mind the colors mentioned in the description - this is the web site colors.
Should not have
• Should not be hard to read

```html
<!DOCTYPE html>
<html lang="en">
<head>
<meta charset="utf-8">
<title>Free Network &amp; Computer Health Check Service</title>
<link href="https://fonts.googleapis.com/css2?family=Oswald:wght@200;300;500;600&family=Arimo:wght@400;700&display=swap" rel="stylesheet">
<style>
  :root {
    --red: #d52b30;
    --red-dark: #9e1518;
    --red-light: #f0494c;
    --frame-gray: #5f5c5d;
    --text-gray: #58585a;
    --ink: #1a1a1a;
    --white: #ffffff;
    --steel-light: #d9dce0;
    --steel-mid: #8a8d92;
    --steel-dark: #3a3b3f;
  }
  * { margin: 0; padding: 0; box-sizing: border-box; }
  html, body { width: 1200px; height: 886px; overflow: hidden; background: var(--frame-gray); }
  .canvas { position: relative; width: 1200px; height: 886px; background: var(--frame-gray); }
  .panel { position: absolute; left: 42px; top: 28px; width: 1117px; height: 828px; background: var(--white); overflow: hidden; }

  .headline-free {
    position: absolute; left: 20px; top: 12px;
    font-family: "Oswald", sans-serif; font-weight: 600;
    font-size: 206px; line-height: 1; letter-spacing: -6px;
    color: var(--red); transform: scaleX(0.84); transform-origin: left top;
  }
  .headline-top {
    position: absolute; left: 334px; top: 34px;
    font-family: "Oswald", sans-serif; font-weight: 300;
    font-size: 94px; line-height: 1; letter-spacing: -1px;
    color: var(--text-gray); text-transform: uppercase; white-space: nowrap;
    transform: scaleX(0.8); transform-origin: left top;
  }
  .headline-bottom {
    position: absolute; left: 334px; top: 110px;
    font-family: "Oswald", sans-serif; font-weight: 600;
    font-size: 92px; line-height: 1; letter-spacing: -1px;
    color: var(--text-gray); text-transform: uppercase; white-space: nowrap;
    transform: scaleX(0.79); transform-origin: left top;
  }
  .headline-bottom .accent { color: var(--red); }

  .checklist { position: absolute; left: 44px; top: 235px; list-style: none; }
  .checklist-item { position: relative; padding-left: 52px; height: 91.5px; }
  .checklist-icon { position: absolute; left: 0; top: 8px; width: 34px; height: 32px; }
  .checklist-title {
    font-family: "Arimo", sans-serif; font-weight: 700;
    font-size: 41px; line-height: 1.1; color: var(--text-gray); white-space: nowrap;
  }
  .checklist-detail {
    font-family: "Arimo", sans-serif; font-weight: 400;
    font-size: 27px; line-height: 1.15; color: var(--ink); white-space: nowrap;
  }

  .tech-illustration {
    position: absolute; left: 719px; top: 325px; width: 368px; height: 329px;
    border-radius: 24px;
    background: linear-gradient(135deg, var(--steel-light) 0%, var(--steel-mid) 40%, var(--steel-dark) 100%);
  }

  .cta-button {
    position: absolute; left: 21px; top: 720px; width: 698px; height: 79px;
    border-radius: 40px; border: 3px solid var(--red-dark);
    background: linear-gradient(to bottom, var(--red-light) 0%, var(--red) 45%, var(--red-dark) 100%);
    box-shadow: 0 4px 6px rgba(0,0,0,0.35);
    display: flex; align-items: center; justify-content: center;
    font-family: "Oswald", sans-serif; font-weight: 500;
    font-size: 60px; line-height: 1; letter-spacing: -0.5px;
    color: var(--white); text-transform: uppercase; text-decoration: none; white-space: nowrap;
  }
  .cta-button span { display: inline-block; transform: scaleX(0.91); }
</style>
</head>
<body>
<div class="canvas">
  <div class="panel">
    <div class="headline-free">FREE</div>
    <div class="headline-top">Network &amp; Computer</div>
    <div class="headline-bottom">Health Check <span class="accent">Service</span></div>

    <ul class="checklist">
      <li class="checklist-item">
        <svg class="checklist-icon" viewBox="0 0 32 30" aria-hidden="true">
          <rect x="2" y="8" width="20" height="20" fill="none" stroke="#58585a" stroke-width="2"/>
          <path d="M6 17 L12 24 L29 3" fill="none" stroke="#d52b30" stroke-width="5" stroke-linecap="round" stroke-linejoin="round"/>
        </svg>
        <div class="checklist-title">Check your network’s security against</div>
        <div class="checklist-detail">hacker attacks, theft, ransomware, viruses, and more.</div>
      </li>
      <li class="checklist-item">
        <svg class="checklist-icon" viewBox="0 0 32 30" aria-hidden="true">
          <rect x="2" y="8" width="20" height="20" fill="none" stroke="#58585a" stroke-width="2"/>
          <path d="M6 17 L12 24 L29 3" fill="none" stroke="#d52b30" stroke-width="5" stroke-linecap="round" stroke-linejoin="round"/>
        </svg>
        <div class="checklist-title">See who and what has</div>
        <div class="checklist-detail">&nbsp;access to your network and data.</div>
      </li>
      <li class="checklist-item">
        <svg class="checklist-icon" viewBox="0 0 32 30" aria-hidden="true">
          <rect x="2" y="8" width="20" height="20" fill="none" stroke="#58585a" stroke-width="2"/>
          <path d="M6 17 L12 24 L29 3" fill="none" stroke="#d52b30" stroke-width="5" stroke-linecap="round" stroke-linejoin="round"/>
        </svg>
        <div class="checklist-title">Perform network</div>
        <div class="checklist-detail">and Internet speed test</div>
      </li>
      <li class="checklist-item">
        <svg class="checklist-icon" viewBox="0 0 32 30" aria-hidden="true">
          <rect x="2" y="8" width="20" height="20" fill="none" stroke="#58585a" stroke-width="2"/>
          <path d="M6 17 L12 24 L29 3" fill="none" stroke="#d52b30" stroke-width="5" stroke-linecap="round" stroke-linejoin="round"/>
        </svg>
        <div class="checklist-title">Resolve PC slowness issues,</div>
        <div class="checklist-detail">security vulnerabilities and improper configurations</div>
      </li>
      <li class="checklist-item">
        <svg class="checklist-icon" viewBox="0 0 32 30" aria-hidden="true">
          <rect x="2" y="8" width="20" height="20" fill="none" stroke="#58585a" stroke-width="2"/>
          <path d="M6 17 L12 24 L29 3" fill="none" stroke="#d52b30" stroke-width="5" stroke-linecap="round" stroke-linejoin="round"/>
        </svg>
        <div class="checklist-title">Validate your backups are</div>
        <div class="checklist-detail">working and recoverable in a timely fashion.</div>
      </li>
    </ul>

    <div class="tech-illustration" role="img" aria-label="Illustration of a dark globe circled by white arrows in front of two server towers with blue lights"></div>

    <a class="cta-button" href="#"><span>Book an Appointment Now!</span></a>
  </div>
</div>
</body>
</html>
```